Ripple Over Tuesday (Podcast Artwork)

We require a podcast cover artwork, to stand out but also make our direction clear. This is a podcast about how everyone can make effective change to help the environment and limit the climate crisis.

The artwork needs to be 3000x3000 pixels for submission to Quillfern Podcasts.

We would ideally like a planet image in there, perhaps within one of the 'o's. However, we are open to suggestions and alternative design options.

The use of green in the artwork would also be good.

```html
<!DOCTYPE html>
<html lang="en">
<head>
<meta charset="utf-8">
<title>Ripple Over Tuesday — Podcast Artwork</title>
<link href="https://fonts.googleapis.com/css2?family=Montserrat:wght@700&display=swap" rel="stylesheet">
<style>
  :root {
    --bg-centre: #5cb51f;
    --bg-edge: #157a08;
    --globe-ocean: #3fa7b8;
    --globe-deep: #1f6f86;
    --globe-land: #8fd13a;
    --title-white: #ffffff;
    --title-shadow: rgba(10, 50, 20, 0.55);
  }
  html, body {
    margin: 0;
    padding: 0;
    overflow: hidden;
  }
  .cover {
    width: 1200px;
    height: 1200px;
    position: relative;
    overflow: hidden;
    background: radial-gradient(circle at 50% 50%, var(--bg-centre) 0%, #3f9a14 55%, var(--bg-edge) 100%);
  }
  .cover-art {
    position: absolute;
    inset: 0;
    width: 1200px;
    height: 1200px;
  }
  .title-word {
    font-family: "Montserrat", sans-serif;
    font-weight: 700;
    fill: var(--title-white);
    text-anchor: middle;
    dominant-baseline: central;
  }
</style>
</head>
<body>
<main class="cover">
  <svg class="cover-art" viewBox="0 0 1200 1200" xmlns="http://www.w3.org/2000/svg">
    <defs>
      <radialGradient id="globe-tone" cx="55%" cy="40%" r="65%">
        <stop offset="0%" stop-color="var(--globe-land)"/>
        <stop offset="35%" stop-color="var(--globe-ocean)"/>
        <stop offset="100%" stop-color="var(--globe-deep)"/>
      </radialGradient>
      <radialGradient id="ground-shadow" cx="50%" cy="50%" r="50%">
        <stop offset="0%" stop-color="rgba(0,40,0,0.35)"/>
        <stop offset="100%" stop-color="rgba(0,40,0,0)"/>
      </radialGradient>
      <filter id="title-drop" x="-20%" y="-20%" width="140%" height="140%">
        <feDropShadow dx="6" dy="8" stdDeviation="7" flood-color="var(--title-shadow)"/>
      </filter>
    </defs>

    <ellipse class="globe-shadow" cx="600" cy="1120" rx="380" ry="40" fill="url(#ground-shadow)"/>

    <circle class="globe-illustration" role="img" aria-label="Painted illustration of planet Earth with green continents and blue oceans"
            cx="588" cy="608" r="480" fill="url(#globe-tone)"/>

    <g class="podcast-title" filter="url(#title-drop)">
      <text class="title-word title-top" x="0" y="0" font-size="200"
            textLength="820" lengthAdjust="spacingAndGlyphs"
            transform="translate(490 378) rotate(-31)">RIPPLE</text>
      <text class="title-word title-middle" x="0" y="0" font-size="150"
            transform="translate(500 585) rotate(-27)">OVER</text>
      <text class="title-word title-bottom" x="0" y="0" font-size="210"
            textLength="1080" lengthAdjust="spacingAndGlyphs"
            transform="translate(640 735) rotate(-27)">TUESDAY</text>
    </g>
  </svg>
</main>
</body>
</html>
```